New Web-Page Design Required

We need a new or initial web design for our page vorlan-grid.com. We provide products & services around infrastructure products. We have two products at the moment, but another 2 in the pipeline.
We want to have the following page structure (and part of the project is to design the 7 pages):
- Home
- Products
-One page per product
- Service
- Support
- About
- Contact (Email form)
The start page should include the following information:
- Twitter / Linkedin Links
- Telephone / Email or in general contact details
- News
- Maybe a link-box, where we can highlight/showcase things
- Link to our support portal, quite prominent
- Testimonials
It would be nice if the product pages would have a image header, where we can put up a screenshot or something. Links to datasheet and videos of the product would be nice as well.
We like the "big banner in the middle" designs, like these two Joomla examples. No need to copy them, it should just give you an idea.
http://www.pelmorthemes.com/itempreview/185
http://www.pelmorthemes.com/content/asj42/index.php
Budget for images available, so please use placeholders or ask us for specific photos/images, if you need them for your design.
Target Market(s)
Business-2-Business, Decision makers and Technical Leads
Industry/Entity Type
News
Look and feel

```html
<!DOCTYPE html>
<html lang="en">
<head>
<meta charset="utf-8">
<title>Vorlan Grid — Home</title>
<link href="https://fonts.googleapis.com/css2?family=Mulish:wght@400;600;700&family=Open+Sans:ital,wght@0,400;0,600;0,700;1,400&display=swap" rel="stylesheet">
<style>
:root{
  --accent:#0db3c4;
  --accent-dark:#0a98a6;
  --ink:#2e2e2e;
  --text:#8a8a8a;
  --line:#e3e3e3;
  --page:#f6f6f6;
  --footer:#4a4a4a;
  --footer-base:#3e3e3e;
  --footer-text:#b9b9b9;
}
*{margin:0;padding:0;box-sizing:border-box}
html,body{width:700px;height:1200px;overflow:hidden}
body{position:relative;background:var(--page);font-family:"Open Sans",sans-serif;color:var(--text)}
.abs{position:absolute}
.heading{font-family:"Mulish",sans-serif;color:var(--ink)}

/* header */
.top-rule{left:0;top:0;width:700px;height:3px;background:var(--accent)}
.site-header{left:0;top:3px;width:700px;height:69px;background:#f9f9f9}
.brand{left:56px;top:19px;display:flex;align-items:center;gap:7px}
.brand-dot{width:28px;height:28px;border-radius:50%;background:var(--accent)}
.brand-name{font-family:"Mulish",sans-serif;font-weight:700;font-size:22px;color:#3a3a3a;letter-spacing:-.3px}
.nav a{position:absolute;top:34px;font-size:9px;color:#333;text-decoration:none}
.nav .current{left:319px;top:0;width:60px;height:70px;background:#e6e6e6;border-bottom:3px solid var(--accent);color:var(--accent);text-align:center;padding-top:34px}

/* hero */
.hero{left:0;top:72px;width:700px;height:257px;background:linear-gradient(90deg,#e9eaeb 0%,#f4f4f4 40%,#eeeeee 70%,#e2e2e2 100%);overflow:hidden;border-bottom:1px solid #d6d6d6}
.hero-person{left:330px;top:45px;width:300px;height:212px;background:linear-gradient(180deg,#d8cbbf 0%,#ececec 45%,#f2f2f2 100%);border-radius:60px 60px 0 0;opacity:.85}
.hero-title{left:77px;top:66px;font-size:0;line-height:0}
.hero-title span{display:block;width:max-content;background:#2f2f2f;color:#fff;font-family:"Mulish",sans-serif;font-weight:600;font-size:15px;line-height:19px;padding:1px 3px;margin-bottom:3px}
.hero-copy{left:77px;top:119px;width:230px;font-size:7.6px;line-height:11.5px;color:#666}
.btn-dark{left:77px;top:158px;width:60px;height:20px;background:#333;color:#fff;font-size:8px;font-weight:600;border-radius:2px;text-align:center;line-height:20px}
.dots{left:84px;top:234px;display:flex;gap:3px}
.dots i{width:7px;height:7px;border-radius:50%;background:#9a9a9a}
.dots i:first-child{background:#1f6f8a}

/* feature boxes */
.feature{top:382px;width:177px;height:83px;border:1px solid #dcdcdc;background:#fff;text-align:center;padding-top:22px}
.feature h3{font-family:"Mulish",sans-serif;font-size:9.5px;font-weight:700;color:#333;letter-spacing:.2px}
.feature p{font-size:6.8px;line-height:10.5px;margin:6px 24px 0}
.feature.active{background:var(--accent);border-color:var(--accent);box-shadow:0 3px 5px rgba(0,0,0,.18)}
.feature.active h3,.feature.active p{color:#fff}
.feature-icon{top:357px;width:36px;height:36px}

/* section titles */
.section-title{font-size:12.5px;font-weight:600;display:flex;align-items:center;white-space:nowrap}
.section-title::after{content:"";flex:1;height:1px;background:var(--line);margin-left:8px}

/* work */
.work-arrows{left:606px;top:502px}
.work-item{top:528px;width:128px;text-align:center}
.work-shot{width:128px;height:95px;background:linear-gradient(180deg,#3a3a3a,#202428);border:1px solid #111}
.work-item h4{font-family:"Mulish",sans-serif;font-size:9px;font-weight:700;color:#333;margin-top:6px}
.work-item small{display:block;font-size:6.6px;color:#999}
.work-item hr{border:0;height:2px;background:#cfcfcf;margin-top:5px}
.work-item.active hr{background:var(--accent)}

/* welcome */
.welcome-copy{left:77px;width:404px;font-size:7.3px;line-height:10.6px}
.btn-accent{background:var(--accent);color:#fff;font-size:7.5px;font-weight:700;text-align:center;border-radius:1px}
.field{left:494px;width:130px;background:#fff;border:1px solid #dedede;font-size:6px;font-style:italic;color:#aaa;padding:4px 6px}

/* lower row */
.bullet-list{left:76px;top:858px;width:176px;list-style:none}
.bullet-list li{height:32px;border-bottom:1px solid var(--line);display:flex;align-items:center;gap:6px;font-size:8.2px;color:#444;white-space:nowrap}
.bullet-list li:last-child{border-bottom:0}
.plus{flex:none;width:12px;height:12px;border-radius:50%;background:var(--accent);color:#fff;font-size:10px;font-weight:700;line-height:12px;text-align:center}
.news{left:272px;width:165px}
.news time{display:block;font-size:6.6px;font-weight:600;color:#555}
.news p{font-size:6.6px;line-height:10px;margin-top:10px;font-weight:600;color:#777}
.news b{color:var(--accent)}
.news-sep{left:263px;top:920px;width:175px;height:1px;background:var(--line)}
.avatar{left:451px;top:864px;width:33px;height:32px;border:1px solid #ccc;background:linear-gradient(180deg,#c9b7a6,#2d3547)}
.cite{left:491px;top:865px;font-size:6.8px;line-height:11px;color:#333}
.cite em{font-family:Georgia,serif;color:#888}
.quote{left:451px;top:905px;width:172px;font-size:7px;line-height:11.5px;color:#777}

/* footer */
.footer{left:0;top:998px;width:700px;height:158px;background:var(--footer)}
.footer-base{left:0;top:1156px;width:700px;height:44px;background:var(--footer-base)}
.f-title{font-size:8.4px;font-weight:400;color:#ddd;display:flex;align-items:center;white-space:nowrap}
.f-title::after{content:"";height:1px;background:#6a6a6a;margin-left:6px;flex:1}
.f-links{list-style:none;font-size:6.6px;line-height:12.3px}
.f-links li{text-decoration:underline;color:var(--footer-text)}
.f-copy{font-size:6.6px;line-height:11.6px;color:var(--footer-text)}
.social{top:1053px;width:19px;height:19px;border-radius:2px;background:var(--accent)}
.newsletter{left:466px;top:1104px;width:156px;height:19px;background:#2e2e2e;border:1px solid #555;font-size:6px;font-style:italic;color:#888;padding:5px 7px}
.newsletter .btn-accent{position:absolute;right:2px;top:2px;width:48px;height:13px;line-height:13px;font-size:7.5px;font-style:normal}
.to-top{left:333px;top:1156px;width:34px;height:17px;background:var(--footer);border-radius:0 0 17px 17px}
.base-text{top:1171px;font-size:7px;color:#8e8e8e}
</style>
</head>
<body>

<div class="abs top-rule"></div>
<header class="abs site-header">
  <div class="abs brand"><span class="brand-dot"></span><span class="brand-name">vorlan grid</span></div>
  <nav class="nav">
    <a class="current">HOME</a>
    <a style="left:387px">Products</a>
    <a style="left:439px">Service</a>
    <a style="left:486px">Support</a>
    <a style="left:534px">About Us</a>
    <a style="left:588px">Contact Us</a>
  </nav>
</header>

<section class="abs hero">
  <div class="abs hero-person" role="img" aria-label="Smiling businessman in white shirt and tie gesturing toward the headline, blurred office background"></div>
  <h1 class="abs hero-title"><span>V.Reports: Check Pulsewire®</span><span>whenever &amp; wherever you like.</span></h1>
  <p class="abs hero-copy">Lorem Ipsum is simply dummy text of the printing and typesetting industry. Lorem Ipsum has been the industry's standard dummy text ever since the 1500s.</p>
  <div class="abs btn-dark">Read More »</div>
  <div class="abs dots"><i></i><i></i><i></i><i></i></div>
</section>

<!-- feature boxes -->
<div class="abs feature" style="left:75px"><h3>PRODUCTS</h3><p>Sed ut perspiciatis unde omnis iste natus error sit voluptatem accusantium doloremque laudantium</p></div>
<div class="abs feature active" style="left:262px"><h3>SUPPORT</h3><p>Sed ut perspiciatis unde omnis iste natus error sit voluptatem accusantium doloremque laudantium</p></div>
<div class="abs feature" style="left:449px"><h3>SERVICE</h3><p>Sed ut perspiciatis unde omnis iste natus error sit voluptatem accusantium doloremque laudantium</p></div>

<svg class="abs feature-icon" style="left:146px" viewBox="0 0 36 36"><circle cx="18" cy="18" r="18" fill="#fff"/><circle cx="18" cy="18" r="16" fill="var(--accent)"/><path d="M10 18l8-7 8 7M12.5 16v8h4v-4h3v4h4v-8" fill="none" stroke="#fff" stroke-width="2" stroke-linejoin="round"/></svg>
<svg class="abs feature-icon" style="left:332px" viewBox="0 0 36 36"><circle cx="18" cy="18" r="18" fill="#fff"/><circle cx="18" cy="18" r="16" fill="#333"/><circle cx="18" cy="18" r="8" fill="none" stroke="#fff" stroke-width="2"/><path d="M10 18h16M18 10v16" stroke="#fff" stroke-width="1.3"/></svg>
<svg class="abs feature-icon" style="left:519px" viewBox="0 0 36 36"><circle cx="18" cy="18" r="18" fill="#fff"/><circle cx="18" cy="18" r="16" fill="var(--accent)"/><circle cx="18" cy="18" r="10" fill="none" stroke="#fff" stroke-width="2"/><path d="M18 12v11M14 19l4 4 4-4" fill="none" stroke="#fff" stroke-width="2" stroke-linecap="round"/></svg>

<!-- work -->
<h2 class="abs heading section-title" style="left:77px;top:499px;width:522px">From Our Work</h2>
<svg class="abs work-arrows" width="20" height="12" viewBox="0 0 20 12"><path d="M6 1L1 6l5 5" fill="none" stroke="#333" stroke-width="1.6"/><path d="M14 1l5 5-5 5" fill="none" stroke="var(--accent)" stroke-width="1.6"/></svg>

<div class="abs work-item" style="left:77px"><div class="work-shot" role="img" aria-label="Dashboard screenshot with availability line chart"></div><h4>Lorem Ipsum Dolor</h4><small>Lorem ipsum</small><hr></div>
<div class="abs work-item active" style="left:217px"><div class="work-shot" role="img" aria-label="Inventory dashboard screenshot with pie and bar charts"></div><h4>Lorem Ipsum Dolor</h4><small>Lorem ipsum</small><hr></div>
<div class="abs work-item" style="left:357px"><div class="work-shot" role="img" aria-label="Server list dashboard screenshot"></div><h4>Lorem Ipsum Dolor</h4><small>Lorem ipsum</small><hr></div>
<div class="abs work-item" style="left:497px"><div class="work-shot" role="img" aria-label="Network traffic dashboard screenshot with line graph"></div><h4>Lorem Ipsum Dolor</h4><small>Lorem ipsum</small><hr></div>

<!-- welcome + quote -->
<h2 class="abs heading section-title" style="left:77px;top:678px;width:404px">Welcome To Vorlan-Grid</h2>
<p class="abs welcome-copy" style="top:701px">Lorem ipsum dolor sit amet, consectetur adipisicing elit, sed do eiusmod tempor incididunt ut labore et dolore magna aliqua. Ut enim ad minim veniam, quis nostrud exercitation ullamco laboris nisi ut aliquip ex ea commodo consequat. Duis aute irure dolor in reprehenderit in voluptate velit esse cillum dolore eu fugiat nulla pariatur. Excepteur sint occaecat cupidatat non proident, sunt in culpa qui officia deserunt mollit anim id est laborum.</p>
<p class="abs welcome-copy" style="top:754px">Lorem ipsum dolor sit amet, consectetur adipisicing elit, sed do eiusmod tempor incididunt ut labore et dolore magna aliqua. Ut enim ad minim veniam, quis nostrud exercitation ullamco commodo consequat. Duis aute irure dolor in reprehenderit in voluptate velit fugiat nulla pariatur.</p>
<div class="abs btn-accent" style="left:77px;top:789px;width:51px;height:18px;line-height:18px">Read More</div>

<h2 class="abs heading section-title" style="left:495px;top:678px;width:129px">Get A Quote</h2>
<div class="abs field" style="top:703px;height:15px;padding-top:3px">Enter your name...</div>
<div class="abs field" style="top:725px;height:15px;padding-top:3px">Enter your email...</div>
<div class="abs field" style="top:746px;height:36px">Enter your comment...</div>
<div class="abs btn-accent" style="left:584px;top:790px;width:40px;height:14px;line-height:14px">Submit</div>

<!-- lower row -->
<h2 class="abs heading section-title" style="left:76px;top:832px;width:176px">Vorlan-Grid</h2>
<ul class="abs bullet-list">
  <li><span class="plus">+</span>Lorem ipsum dolor sit amet consectetur</li>
  <li><span class="plus">+</span>Adipiscing elit, Sed do eiusmod</li>
  <li><span class="plus">+</span>Tempor incididunt ut labore</li>
  <li><span class="plus">+</span>Et dolor magna aliqua</li>
</ul>

<h2 class="abs heading section-title" style="left:263px;top:832px;width:175px">News &amp; Events</h2>
<article class="abs news" style="top:862px"><time>5th January 2013</time><p><b>Integer mauris.</b> Cras iaculis viverra dolorqw. Nulla suscipit. Proin eu sapien ac sem fermentum sollicitudin.</p></article>
<div class="abs news-sep"></div>
<article class="abs news" style="top:927px"><time>8th January 2013</time><p><b>Integer mauris.</b> Cras iaculis viverra dolor. Nulla suscipit. Proin eu sapien ac sem fermentum sollicitudin.</p></article>

<h2 class="abs heading section-title" style="left:450px;top:832px;width:174px">Testimonials</h2>
<div class="abs avatar" role="img" aria-label="Portrait photo of the client giving the testimonial"></div>
<p class="abs cite">Martin Kessel<br>Managing Director XYZ<br><em>kesselworks.co.au</em></p>
<p class="abs quote">“Donec sed odio dui. Nulla vitae elit libero, a pharetra augue. Nullam id dolor id nibh ultricies vehicula ut id elit. Integer posuere erat a ante venenatis dapibus ponec sed odio dui. Nulla vitae elit libero, a pharetra augue....”</p>

<!-- footer -->
<footer class="abs footer"></footer>
<h3 class="abs f-title" style="left:78px;top:1026px;width:60px">Links</h3>
<ul class="abs f-links" style="left:78px;top:1049px"><li>Home</li><li>Products</li><li>Service</li><li>Support</li><li>About Us</li><li>Contact Us</li></ul>

<h3 class="abs f-title" style="left:178px;top:1026px;width:123px">About Us</h3>
<p class="abs f-copy" style="left:178px;top:1047px;width:130px">Lorem ipsum dolor sit amet, consectetur adipisicing elit, sed do eiusmod tempor incididunt ut labore et dolore magna aliqua. Ut enim ad minim veniam, quis nostrud exercitation ullamco laboris nisi ut aliquip ex ea commodo consequat.</p>

<h3 class="abs f-title" style="left:355px;top:1026px;width:75px">Contact Info</h3>
<ul class="abs f-links" style="left:355px;top:1049px;line-height:11.6px"><li>Lorem ipsum</li><li>dolor sit amet 106</li><li>1404 lorem ipsum dolor</li><li>sit amet</li><li>email:</li><li>info@vorlan-grid.com</li><li>Phone: 1-800-555-0142</li></ul>

<h3 class="abs f-title" style="left:466px;top:1026px;width:156px">Stay updates on our Socail Network</h3>
<span class="abs social" style="left:466px" role="img" aria-label="Social network link"></span>
<span class="abs social" style="left:493px" role="img" aria-label="Social network link"></span>
<span class="abs social" style="left:519px" role="img" aria-label="Social network link"></span>

<h3 class="abs f-title" style="left:466px;top:1085px;width:156px">Join Our Newsletter</h3>
<div class="abs newsletter">Enter your email address<span class="btn-accent">Subscribe</span></div>

<div class="abs footer-base"></div>
<div class="abs to-top"><svg width="34" height="14" viewBox="0 0 34 14"><path d="M12 9l5-5 5 5" fill="none" stroke="#888" stroke-width="1.3"/></svg></div>
<p class="abs base-text" style="left:78px">© Copyrights 2013 All rights Reserved</p>
<p class="abs base-text" style="left:521px">Privacy Policy &amp; Terms of uses</p>

</body>
</html>
```